Quarrow financial services, is a financial company that provides consultancy, brokerage services, and funding.

we will be providing the clients with insights, knowledge and data with regards to the financial markets.

with the brokerage services we will try to find the suitable counterparts that provide them with the best investments that suits their needs and expected return.

Target Market(s)

financial institutions, Corporates, high-net worth individuals

Industry/Entity Type

Financial Service

Contact Information for Business Card

Font styles to use
Other font styles liked:
• applemyungjo

Colors
00a990
848484

Requirements
Must have
• the logo at the back
Nice to have
• Finesse
Should not have
• boldness

```html
<!DOCTYPE html>
<html lang="en">
<head>
<meta charset="utf-8">
<title>Quarrow Financial Services — Business Card</title>
<link rel="stylesheet" href="https://fonts.googleapis.com/css2?family=Cinzel:wght@400;500&family=Open+Sans:wght@400;600&display=swap">
<style>
  :root {
    --canvas: #e9e7e4;
    --card: #1f2a33;
    --ink: #ffffff;
    --ink-soft: #e6ebee;
    --accent: #8cc36a;
    --shadow: rgba(0, 0, 0, 0.28);
  }
  * { box-sizing: border-box; margin: 0; padding: 0; }
  html, body {
    width: 1200px; height: 900px; overflow: hidden;
    background: var(--canvas);
  }
  .stage { position: relative; width: 1200px; height: 900px; }
  .card {
    position: absolute;
    background: var(--card);
    box-shadow: 0 6px 18px var(--shadow);
    color: var(--ink);
  }
  .card--front { left: 238px; top: 62px; width: 555px; height: 342px; }
  .card--back  { left: 457px; top: 518px; width: 560px; height: 342px; }

  /* front */
  .front-brand {
    position: absolute; left: 112px; top: 152px;
    display: flex; align-items: center; gap: 10px;
    font-family: "Open Sans", sans-serif; font-weight: 400;
    font-size: 26px; color: var(--ink);
  }
  .brand-square { width: 14px; height: 14px; background: var(--accent); }
  .contact {
    position: absolute; left: 291px; top: 86px;
    font-family: "Open Sans", sans-serif; font-size: 15px; line-height: 20px;
    color: var(--ink-soft);
  }
  .contact__name { font-weight: 600; font-size: 18px; color: var(--ink); line-height: 22px; }
  .contact__title { line-height: 18px; }
  .contact__address { margin-top: 13px; }
  .contact__lines { margin-top: 14px; list-style: none; }
  .contact__lines li { display: flex; align-items: center; gap: 8px; }
  .contact__lines svg { width: 12px; height: 12px; fill: var(--ink-soft); flex: none; }

  /* back */
  .back-mark {
    position: absolute; left: 270px; top: 128px;
    width: 20px; height: 20px; background: var(--accent);
  }
  .back-name {
    position: absolute; left: 0; right: 0; top: 200px; text-align: center;
    font-family: "Cinzel", serif; font-weight: 400; font-size: 44px;
    letter-spacing: 2px; color: var(--ink); line-height: 1;
  }
  .back-sub {
    position: absolute; left: 0; right: 0; top: 244px; text-align: center;
    font-family: "Cinzel", serif; font-size: 14px; letter-spacing: 2.5px;
    color: var(--ink);
  }
  .back-tagline {
    position: absolute; left: 0; right: 0; top: 264px; text-align: center;
    font-family: "Cinzel", serif; font-size: 11px; letter-spacing: 0.3px;
    color: var(--ink);
  }
</style>
</head>
<body>
<main class="stage">
  <section class="card card--front" aria-label="Business card front">
    <div class="front-brand"><span class="brand-square"></span>Quarrow</div>
    <div class="contact">
      <p class="contact__name">Daniel Hartley</p>
      <p class="contact__title">Managing Director</p>
      <p class="contact__address">12345, Address Goes Here<br>Country Name, 123456.</p>
      <ul class="contact__lines">
        <li><svg viewBox="0 0 24 24" aria-hidden="true"><path d="M6.6 10.8a15 15 0 0 0 6.6 6.6l2.2-2.2a1 1 0 0 1 1-.25 11.4 11.4 0 0 0 3.6.57 1 1 0 0 1 1 1V20a1 1 0 0 1-1 1A17 17 0 0 1 3 4a1 1 0 0 1 1-1h3.5a1 1 0 0 1 1 1c0 1.25.2 2.45.57 3.57a1 1 0 0 1-.25 1z"/></svg>020-555 018 462</li>
        <li><svg viewBox="0 0 24 24" aria-hidden="true"><path d="M2 5h20v14H2z M2 5l10 8 10-8" fill="none" stroke="#e6ebee" stroke-width="2.5"/></svg>info@quarrowfs.com</li>
        <li><svg viewBox="0 0 24 24" aria-hidden="true"><circle cx="12" cy="12" r="10"/></svg>www.quarrowfs.com</li>
      </ul>
    </div>
  </section>

  <section class="card card--back" aria-label="Business card back">
    <div class="back-mark"></div>
    <h1 class="back-name">QUARROW</h1>
    <p class="back-sub">FINANCIAL SERVICES</p>
    <p class="back-tagline">YOUR CAPITAL GUIDED WITH CARE AND CLARITY</p>
  </section>
</main>
</body>
</html>
```